Werbebrief
Zielgruppe
Unsere Zielgruppe sind Geschäftsführer junger Unternehmen.
Hallo,
Wir benötigen einen "Werbebrief". Es ist jedoch weniger ein Brief, als viel mehr eine etwas größerer "Werbekarte" (diese soll 105 x 210mm groß sein).
Auf der Vorderseite soll folgender Text stehen:
Für Unternehmen, die gerne expandieren möchten
Auf der Rückseite soll folgender Link stehen:
www.tolvek-werk.de/Expandieren
Darunter soll folgendes stehen:
Ihr persönlicher Code: ABC123
Wichtig ist, dass wir den Code individuell ändern können, da jeder einen anderen Code bekommt.
Unser Logo und Corporate Farbe habe ich hochgeladen. Das Design sollte auf jeden Fall zu unserer Webseite passen (www.tolvek-werk.de)
Wir freuen uns auf Ihre Vorschläge.

```html
<!DOCTYPE html>
<html lang="de">
<head>
<meta charset="utf-8">
<title>Tolvek Werk – Werbekarte</title>
<link rel="stylesheet" href="https://fonts.googleapis.com/css2?family=Open+Sans:wght@400;600&display=swap">
<style>
  :root {
    --page-bg: #e9e6e1;
    --card-blue-light: #2c5ca6;
    --card-blue-dark: #1b4585;
    --ink-white: #ffffff;
    --line-white: rgba(255,255,255,0.95);
    --line-soft: rgba(255,255,255,0.35);
  }
  * { margin: 0; padding: 0; box-sizing: border-box; }
  html, body {
    width: 1200px; height: 1200px; overflow: hidden;
    background: var(--page-bg);
    font-family: "Open Sans", sans-serif;
    color: var(--ink-white);
  }
  .sheet {
    position: relative; width: 1200px; height: 1200px;
    display: flex; flex-direction: column; align-items: center; justify-content: center; gap: 60px;
  }
  .card {
    position: relative; width: 960px; height: 480px;
    background: radial-gradient(ellipse at 50% 35%, var(--card-blue-light) 0%, var(--card-blue-dark) 100%);
    box-shadow: 0 6px 18px rgba(0,0,0,0.25);
    overflow: hidden;
  }
  .brand {
    position: absolute; top: 38px; right: 48px;
    display: flex; align-items: center; gap: 12px;
    font-size: 30px; font-weight: 400; letter-spacing: 0.3px;
  }
  .brand-dot { width: 14px; height: 14px; border-radius: 50%; background: var(--ink-white); }
  .rule { position: absolute; left: 0; width: 100%; height: 4px; }
  .rule--fade-right { background: linear-gradient(90deg, var(--line-white) 0%, var(--line-white) 45%, rgba(255,255,255,0) 100%); }
  .rule--fade-left { background: linear-gradient(90deg, rgba(255,255,255,0) 0%, var(--line-white) 55%, var(--line-white) 100%); }
  .rule--soft { height: 3px; background: linear-gradient(90deg, rgba(255,255,255,0) 5%, var(--line-soft) 50%, rgba(255,255,255,0) 95%); }

  .front .rule--upper { top: 168px; }
  .front .rule--lower { top: 338px; }
  .front .headline {
    position: absolute; top: 196px; left: 0; width: 100%;
    text-align: center; font-size: 46px; line-height: 1.22; font-weight: 400;
    padding-left: 120px;
  }

  .back .url { position: absolute; top: 118px; left: 60px; font-size: 23px; }
  .back .rule--upper { top: 162px; }
  .back .rule--middle { top: 288px; }
  .back .rule--lower { top: 352px; }
  .back .code {
    position: absolute; top: 196px; left: 50px;
    font-size: 46px; font-weight: 400;
  }
  .back .code-value { font-variant-numeric: oldstyle-nums; }
  .back .note {
    position: absolute; top: 372px; right: 52px; width: 370px;
    font-size: 20px; line-height: 1.3;
  }
</style>
</head>
<body>
<main class="sheet">
  <section class="card front">
    <div class="brand"><span class="brand-dot"></span><span class="brand-name">Tolvek Werk</span></div>
    <div class="rule rule--upper rule--fade-right"></div>
    <h1 class="headline">Für Unternehmen, die gerne<br>expandieren möchten</h1>
    <div class="rule rule--lower rule--soft"></div>
  </section>

  <section class="card back">
    <div class="brand"><span class="brand-dot"></span><span class="brand-name">Tolvek Werk</span></div>
    <p class="url">www.tolvek-werk.de/Expandieren</p>
    <div class="rule rule--upper rule--fade-right"></div>
    <p class="code">Ihr persönlicher Code: <span class="code-value">Mar1612</span></p>
    <div class="rule rule--middle rule--soft"></div>
    <div class="rule rule--lower rule--fade-left"></div>
    <p class="note">Wichtig ist, dass wir den Code individuell ändern können, da jeder einen anderen Code bekommt.</p>
  </section>
</main>
</body>
</html>
```